Business IT Services Billboard to attract local small businesses

We are Brivolane, a premier Managed Service Provider (MSP) specializing in comprehensive IT services and VOIP phone solutions exclusively for businesses. Our goal is to create a dynamic and visually engaging billboard advertisement that not only highlights our cutting-edge IT solutions but also emphasizes our state-of-the-art VOIP phone services. This billboard should communicate our commitment to providing innovative, reliable, and holistic technology solutions.
Target Market(s)
small business
Industry/Entity Type
Information Technology
Colors
Designer to choose colors to be used in the design.
Look and feel
Each slider illustrates characteristics of the customer's brand and the style your logo design should communicate.

```html
<!DOCTYPE html>
<html lang="en">
<head>
<meta charset="UTF-8">
<title>Brivolane – IT and VOIP Billboard</title>
<link href="https://fonts.googleapis.com/css2?family=Open+Sans:wght@400&family=Roboto:wght@300&family=Roboto+Condensed:wght@300;700&display=swap" rel="stylesheet">
<style>
  :root {
    --page-bg: #e4e4e4;
    --board-top: #eaf3fc;
    --board-bottom: #ffffff;
    --brand-blue: #0f6cbd;
    --deep-blue: #0b63b3;
    --cyan: #1fb6ee;
    --ink: #222428;
    --white: #ffffff;
    --suit-dark: #141b26;
    --suit-mid: #2a3544;
  }
  * { margin: 0; padding: 0; box-sizing: border-box; }
  html, body {
    width: 1071px;
    height: 1200px;
    overflow: hidden;
    background: var(--page-bg);
  }
  .canvas {
    position: relative;
    width: 1071px;
    height: 1200px;
  }
  .billboard {
    position: absolute;
    left: 35px;
    top: 381px;
    width: 1000px;
    height: 437px;
    overflow: hidden;
    background: linear-gradient(180deg, var(--board-top) 0%, var(--board-bottom) 70%);
    box-shadow: 0 10px 18px rgba(0,0,0,0.12);
  }
  .portrait {
    position: absolute;
    left: 560px;
    top: 0;
    width: 440px;
    height: 100%;
    background:
      linear-gradient(90deg, rgba(255,255,255,0) 0%, rgba(255,255,255,0) 8%, var(--suit-mid) 34%, var(--suit-dark) 60%, var(--suit-mid) 100%);
  }
  .brand-name {
    position: absolute;
    left: 38px;
    top: 36px;
    font-family: "Roboto Condensed", sans-serif;
    font-weight: 700;
    font-size: 58px;
    letter-spacing: 14px;
    line-height: 1;
    color: var(--brand-blue);
  }
  .headline {
    position: absolute;
    left: 38px;
    top: 136px;
    font-family: "Roboto", sans-serif;
    font-weight: 300;
    font-size: 55px;
    line-height: 51px;
    color: var(--ink);
  }
  .headline strong {
    font-family: "Roboto Condensed", sans-serif;
    font-weight: 700;
    color: var(--brand-blue);
    font-size: 57px;
  }
  .subline {
    position: absolute;
    left: 38px;
    top: 314px;
    font-family: "Open Sans", sans-serif;
    font-weight: 400;
    font-size: 23.5px;
    line-height: 31px;
    color: var(--ink);
  }
  .bottom-band {
    position: absolute;
    left: 0;
    top: 0;
    width: 1000px;
    height: 437px;
  }
  .call-to-action {
    position: absolute;
    right: 30px;
    top: 392px;
    font-family: "Roboto Condensed", sans-serif;
    color: var(--white);
    white-space: nowrap;
    line-height: 1;
  }
  .call-to-action .lead {
    font-weight: 300;
    font-size: 18px;
  }
  .call-to-action .web-address {
    font-weight: 700;
    font-size: 25px;
    margin-left: 3px;
  }
</style>
</head>
<body>
<main class="canvas">
  <section class="billboard">
    <div class="portrait" role="img" aria-label="Photo of a businessman in a dark suit and tie touching a floating cluster of blue hexagon service icons, the largest reading VOIP"></div>

    <svg class="bottom-band" viewBox="0 0 1000 437" aria-hidden="true">
      <polygon points="0,390 520,402 520,437 0,437" fill="var(--cyan)"/>
      <polygon points="0,432 1000,358 1000,437 0,437" fill="var(--deep-blue)"/>
    </svg>

    <h1 class="brand-name">BRIVOLANE</h1>

    <h2 class="headline">
      Elevate Your Business<br>
      with <strong>Next-Gen IT</strong> and<br>
      <strong>VOIP Services</strong>
    </h2>

    <p class="subline">
      Innovative&nbsp; IT and VOIP Solutions<br>
      Tailored for Your Business Success.
    </p>

    <p class="call-to-action">
      <span class="lead">Transform Your Tech Today at</span><span class="web-address">www.brivolane.com</span>
    </p>
  </section>
</main>
</body>
</html>
```